Business Card Design for DJ

Double-sided full colour business card, with containing the following key information:

DJ Plumwire
Phone (###) ###-####
Email: djplumwire@quillpost.com
Chatterloom: chatterloom.com/djplumwire
Chirpline: @djplumwire

Bringing you the best in Top 40 - Retro - Funk

"It's gonna be a plumwire."

Club/Bar – Weddings – Private Parties - Corporate Events
3000W of portable sound
Dancefloor lighting with optional custom gobos
Available HD Projector and screen
Available custom video production
Free consultation

ERSB Licensed (small logo from http://www.ersbrights.ca)
Member of MNTRK (small logo from http://www.mntrkguild.ca)

• DJ Plumwire logo (attached) or alternative wordmark using type similar to CLUBLAND at http://tunevaultzone.net/uploads/posts/1226228091_6705615x.jpg
• headshot (attached), dance club look/feel

```html
<!DOCTYPE html>
<html lang="en">
<head>
<meta charset="utf-8">
<title>DJ Plumwire – Business Card</title>
<link rel="stylesheet" href="https://fonts.googleapis.com/css2?family=Alegreya+Sans+SC:wght@400;500&display=swap">
<style>
  :root {
    --card-bg: #000000;
    --title-pink: #c23a72;
    --contact-pink: #dba0c4;
    --tagline-pink: #d0457e;
    --art-deep: #5a0f2c;
    --art-bright: #c8245e;
    --card-font: "Alegreya Sans SC", "Trebuchet MS", sans-serif;
  }
  html, body {
    margin: 0;
    padding: 0;
    width: 1200px;
    height: 800px;
    overflow: hidden;
    background: var(--card-bg);
  }
  .card {
    position: relative;
    width: 1200px;
    height: 800px;
    background: var(--card-bg);
    font-family: var(--card-font);
    overflow: hidden;
  }
  .card__title {
    position: absolute;
    left: 64px;
    top: 72px;
    margin: 0;
    font-weight: 500;
    font-size: 76px;
    line-height: 1;
    letter-spacing: 6px;
    color: var(--title-pink);
  }
  .card__contact {
    position: absolute;
    left: 0;
    top: 248px;
    width: 760px;
    margin: 0;
    text-align: center;
    font-style: normal;
    font-size: 32px;
    line-height: 46px;
    letter-spacing: 2.5px;
    color: var(--contact-pink);
  }
  .card__contact span { display: block; }
  .card__art {
    position: absolute;
    left: 806px;
    top: 0;
    width: 380px;
    height: 412px;
  }
  .card__quote {
    position: absolute;
    left: 226px;
    top: 572px;
    margin: 0;
    font-size: 42px;
    letter-spacing: 3px;
    color: var(--tagline-pink);
  }
  .card__services {
    position: absolute;
    left: 0;
    top: 704px;
    width: 1200px;
    margin: 0;
    text-align: center;
    font-size: 42px;
    letter-spacing: 3px;
    color: var(--tagline-pink);
    white-space: nowrap;
  }
</style>
</head>
<body>
  <main class="card">
    <h1 class="card__title">Dj Plumwire</h1>

    <address class="card__contact">
      <span>DJ Plumwire</span>
      <span>Phone (###) ###-####</span>
      <span>Email: djplumwire@quillpost.com</span>
      <span>Chatterloom: chatterloom.com/djplumwire</span>
      <span>Chirpline: @djplumwire</span>
    </address>

    <svg class="card__art" viewBox="0 0 380 412" role="img" aria-label="Line illustration of a DJ wearing headphones, scratching a vinyl record on a turntable">
      <defs>
        <radialGradient id="art-glow" cx="55%" cy="50%" r="60%">
          <stop offset="0%" stop-color="var(--art-bright)" stop-opacity="0.55"/>
          <stop offset="100%" stop-color="var(--art-deep)" stop-opacity="0.15"/>
        </radialGradient>
      </defs>
      <rect x="0" y="0" width="380" height="412" rx="24" fill="url(#art-glow)"/>
    </svg>

    <p class="card__quote">"Its going to be a PlumWire</p>

    <p class="card__services">Bringing You the best Top 40 - Retro - Funk</p>
  </main>
</body>
</html>
```